Real Estate Company
Tolin Estate Partners
Project: Real Estate Company
Real Estate Company - Real Estate
Creative Brief
Professional
Dale Moxon
Broker
PO Box 3152 Fresno, CA 93729
dale@tolinestatepartners.com
www.tolinestatepartners.com
BRE # 04527391
Card should have rounded edges.
one side of card should have all the info and one side should have logo + website

```html
<!DOCTYPE html>
<html lang="en">
<head>
<meta charset="utf-8">
<title>Tolin Estate Partners – Business Card</title>
<link href="https://fonts.googleapis.com/css2?family=Exo+2:wght@400;500;600&family=Open+Sans:wght@400;600&display=swap" rel="stylesheet">
<style>
  :root {
    --backdrop: #c9cacc;
    --card: #ffffff;
    --frame: #9a9da2;
    --blue: #1f86d6;
    --blue-light: #4fb0ef;
    --blue-deep: #1466b3;
    --charcoal: #3d3f43;
    --ink: #45484d;
    --brand: #1d6fb8;
  }
  * { margin: 0; padding: 0; box-sizing: border-box; }
  html, body { width: 1200px; height: 895px; overflow: hidden; }
  body {
    background: var(--backdrop);
    font-family: "Open Sans", sans-serif;
    color: var(--ink);
    position: relative;
  }
  .card {
    position: absolute;
    left: 250px;
    width: 700px;
    height: 400px;
    background: var(--card);
    border-radius: 18px;
    overflow: hidden;
    box-shadow: 0 6px 18px rgba(0,0,0,0.18);
  }
  .card--back { top: 30px; }
  .card--front { top: 465px; }

  .frame {
    position: absolute;
    inset: 22px;
    border: 2px solid var(--frame);
  }

  /* Back side */
  .back-logo {
    position: absolute;
    top: 80px;
    left: 0; right: 0;
    display: flex;
    justify-content: center;
    align-items: center;
    gap: 14px;
  }
  .brand-mark {
    width: 30px; height: 30px;
    background: var(--brand);
    flex: none;
  }
  .brand-name {
    font-family: "Exo 2", sans-serif;
    font-weight: 600;
    color: var(--brand);
    letter-spacing: 1px;
    white-space: nowrap;
  }
  .back-logo .brand-name { font-size: 34px; }
  .back-band {
    position: absolute;
    left: 0; right: 0;
    top: 215px;
    height: 80px;
    background: linear-gradient(90deg, var(--blue-deep), var(--blue) 40%, var(--blue-light));
    display: flex;
    align-items: center;
    justify-content: center;
  }
  .back-band .website {
    font-family: "Exo 2", sans-serif;
    font-size: 26px;
    color: #fff;
    letter-spacing: 1px;
  }

  /* Front side */
  .front-logo {
    position: absolute;
    top: 58px;
    left: 60px;
    display: flex;
    align-items: center;
    gap: 10px;
  }
  .front-logo .brand-mark { width: 22px; height: 22px; }
  .front-logo .brand-name { font-size: 24px; }

  .contact {
    position: absolute;
    display: flex;
    flex-direction: column;
    gap: 14px;
    font-size: 15px;
  }
  .contact--left { left: 60px; top: 150px; }
  .contact--right { left: 370px; top: 218px; }
  .contact-row { display: flex; align-items: center; gap: 10px; white-space: nowrap; }
  .icon {
    width: 22px; height: 22px;
    border-radius: 5px;
    background: var(--blue);
    flex: none;
    display: flex; align-items: center; justify-content: center;
  }
  .icon svg { width: 14px; height: 14px; }
  .person {
    position: absolute;
    left: 370px;
    top: 120px;
  }
  .person-name {
    font-family: "Exo 2", sans-serif;
    font-size: 26px;
    font-weight: 500;
    color: var(--blue);
    line-height: 1.2;
  }
  .person-title { font-size: 16px; color: var(--ink); line-height: 1.4; }
  .person-licence { font-size: 14px; color: var(--ink); line-height: 1.4; }

  .front-band {
    position: absolute;
    left: 0; right: 0; bottom: 0;
    height: 60px;
    background: linear-gradient(90deg, var(--blue-deep), var(--blue) 45%, var(--blue-light));
  }
  .front-tab {
    position: absolute;
    left: 0; bottom: 60px;
    width: 110px; height: 60px;
    background: var(--charcoal);
    clip-path: polygon(0 0, 55% 0, 100% 100%, 0 100%);
  }
</style>
</head>
<body>

  <section class="card card--back" aria-label="Card back">
    <div class="frame"></div>
    <div class="back-logo">
      <span class="brand-mark"></span>
      <span class="brand-name">TOLIN ESTATE PARTNERS</span>
    </div>
    <div class="back-band"><span class="website">www.tolinestatepartners.com</span></div>
  </section>

  <section class="card card--front" aria-label="Card front">
    <div class="frame"></div>
    <div class="front-tab"></div>
    <div class="front-band"></div>

    <div class="front-logo">
      <span class="brand-mark"></span>
      <span class="brand-name">TOLIN ESTATE PARTNERS</span>
    </div>

    <div class="contact contact--left">
      <div class="contact-row">
        <span class="icon"><svg viewBox="0 0 24 24"><path fill="#fff" d="M6.6 10.8a15 15 0 0 0 6.6 6.6l2.2-2.2a1 1 0 0 1 1-.25 11.4 11.4 0 0 0 3.6.57 1 1 0 0 1 1 1V20a1 1 0 0 1-1 1A17 17 0 0 1 3 4a1 1 0 0 1 1-1h3.5a1 1 0 0 1 1 1c0 1.25.2 2.45.57 3.57a1 1 0 0 1-.25 1z"/></svg></span>
        <span>559 555 0148</span>
      </div>
      <div class="contact-row">
        <span class="icon"><svg viewBox="0 0 24 24"><path fill="#fff" d="M3 5h18v14H3z"/><path fill="none" stroke="#1f86d6" stroke-width="2" d="M3 6l9 7 9-7"/></svg></span>
        <span>dale@tolinestatepartners.com</span>
      </div>
    </div>

    <div class="person">
      <div class="person-name">Dale Moxon</div>
      <div class="person-title">Broker</div>
      <div class="person-licence">BRE # 04527391</div>
    </div>

    <div class="contact contact--right">
      <div class="contact-row">
        <span class="icon"><svg viewBox="0 0 24 24"><path fill="#fff" d="M12 2a7 7 0 0 0-7 7c0 5 7 13 7 13s7-8 7-13a7 7 0 0 0-7-7zm0 9.5A2.5 2.5 0 1 1 12 6.5a2.5 2.5 0 0 1 0 5z"/></svg></span>
        <span>PO Box 3152 Fresno, CA 93729</span>
      </div>
      <div class="contact-row">
        <span class="icon"><svg viewBox="0 0 24 24"><g fill="none" stroke="#fff" stroke-width="2"><circle cx="12" cy="12" r="9"/><path d="M3 12h18M12 3c3 3 3 15 0 18M12 3c-3 3-3 15 0 18"/></g></svg></span>
        <span>www.tolinestatepartners.com</span>
      </div>
    </div>
  </section>

</body>
</html>
```